Thornbeck Advisory Group Business Card Design Project

2-sided business card for my small (me and a couple subcontractors) firm, which consults to public community colleges and school districts and public agencies in California on energy matters, mostly solar electric systems that can reduce their electricity use by as much as 80%. I prepare requests for proposals (RFPs), manage the RFP processes, and work with the solar vendors to get the best deal for my clients. I also do regulatory and legislative advocacy for strong renewable energy policies. I do lots of quantitative analysis to make sure the solar systems are sized to produce the maximum monetary savings and focus a lot on the aesthetic design of the solar systems, as architectural features of the campuses (most are carport structures built in parking lots, but some are built on the ground and on rooftops). All my work is geared to getting the best value, highest quality, and most reliable solar system. My career background is in public interest energy advocacy; I'm not a consultant trying to make a million dollars but someone who is still serving in the public interest.

My competition is made up of much larger firms; this business card/logo in large part is intended to present an image of my firm as an equal to these larger firms despite my smaller size.

Essential information as follows:
Firm name: Thornbeck Advisory Group
Tagline: Clean Energy Procurement for the Public Sector
Name: Walter Pennick
email, 2 phone number, and address listed as well.

Target Market(s)

Public schools, community colleges, & public agencies.There is a wide range in the sophistication of these organizations.

Industry/Entity Type

Parking

Requirements
Must have
• - several rich colors, which can be either in the logo or in the background - the overall feeling of the card should reflect richness of color. I have uploaded some photos showing some colors that I like together. By rich I do not necessarily mean bright. I suppose bright colors in the logo could be supported with rich colors in the overall background of the card.
- professional, and powerful in an understated way (not kooky, cartoonish, or very playful)
- the logo must NOT be too representational of solar energy or the sun, but at the same time it would be good for the logo to be somewhat suggestive of this.

Nice to have
• -I like abstract and geometric images (with rich colts).
- A very subtle reference to schools/colleges/education would be great but it CANNOT be explicit; it would have to be faintly suggestive.
- In the logo I like the idea of abstract or geometric shapes intersecting with other in an interesting and suggestive way, conveying the multiple aspects of my practice (economics, data analysis, energy analysis, problem solving, managing collaborative processes, policy analysis)
- My work relates to environmental concerns, especially climate change. Working this into the logo in a subtle way could be good, but it's not a requirement.
- I like the idea that the logo/card feels serene.
- In designing the business card, I kind of like the idea of having the tag line as the first thing they read, then they see the firm name.

Should not have
• Not:
- humorous
- boring
- overly slick
- overly formal
- whimsical

```html
<!DOCTYPE html>
<html lang="en">
<head>
<meta charset="utf-8">
<title>Thornbeck Advisory Group — Business Card</title>
<link href="https://fonts.googleapis.com/css2?family=Quicksand:wght@300&display=swap" rel="stylesheet">
<style>
  :root {
    --paper: #ffffff;
    --sky-blue: #229be8;
    --sun-amber: #fbaf3f;
    --ink-light: #ffffff;
  }
  html, body {
    margin: 0;
    padding: 0;
    overflow: hidden;
    background: var(--paper);
  }
  .card {
    position: relative;
    width: 1200px;
    height: 726px;
    overflow: hidden;
    background: var(--paper);
    font-family: "Quicksand", sans-serif;
    font-weight: 300;
    color: var(--ink-light);
  }
  .card-face {
    position: absolute;
    left: 154px;
    top: 0;
    width: 1046px;
    height: 726px;
    background: var(--sky-blue);
    overflow: hidden;
  }
  .sun-disc {
    position: absolute;
    left: 0;
    top: 0;
  }
  .tagline {
    position: absolute;
    left: 73px;
    top: 106px;
    margin: 0;
    font-size: 50px;
    font-weight: 300;
    line-height: 63px;
    letter-spacing: 2.4px;
    white-space: nowrap;
  }
  .wordmark {
    position: absolute;
    left: 0;
    top: 0;
  }
  .wordmark-name {
    position: absolute;
    left: 632px;
    top: 520px;
    font-size: 62px;
    line-height: 1;
    letter-spacing: 2px;
    white-space: nowrap;
  }
  .wordmark-descriptor {
    position: absolute;
    left: 608px;
    top: 590px;
    font-size: 27px;
    line-height: 1;
    letter-spacing: 1.6px;
    white-space: nowrap;
  }
</style>
</head>
<body>
  <div class="card">
    <section class="card-face">
      <svg class="sun-disc" width="1046" height="726" viewBox="0 0 1046 726" aria-hidden="true">
        <circle cx="791" cy="595" r="306" fill="var(--sun-amber)"/>
      </svg>
      <h1 class="tagline">Clean Energy Procurement<br>for the Public Sector</h1>
      <div class="wordmark">
        <span class="wordmark-name">Thornbeck</span>
        <span class="wordmark-descriptor">Advisory Group</span>
      </div>
    </section>
  </div>
</body>
</html>
```